Wedding and event Photography company.

We need a business card design for a photography company based in Singapore named LumaVek. Our core service offering is wedding photojournalism. We would like to see minimalistic designs that use the colour white. The final design should communicate a sense of ease and reliability.

The attached are a couple of visual reference which i found over the web, i hope it will helps.

Project Brief Update (14th July 2014):
- Please refrain from using any images from the website for the design. The laws and regulations over here does not allow me to distribute my client's images. Thanks!

Target Market(s)

Young and middle aged adults aged 24 - 38. With money to spend =D

Industry/Entity Type

Business

Contact Information for Business Card

Name: Dax Pell
Designation: Head Photographer
Mobile: +65 84126079
Email: tan@lumavek.example
Website: www.lumavek.example

Font styles to use
Other font styles liked:
• Baskerville URW

Colors

Designer to choose colors to be used in the design.

Requirements
Must have
• Must include:
• - The brand LumaVek
• - The logo attached
• - Please help to place the brand LumaVek with the logo according to your preferences.
• - Services
• - Wedding Photography
• - Portraiture
• - Photojournalism
Nice to have
• Looking forward to an elegant and simple design. Please see attached examples!
• Please use Serif Fonts
Should not have
• Please refrain from using dark tones for the majority of the design.
• Please refrain from letterpress and embossing.

```html
<!DOCTYPE html>
<html lang="en">
<head>
<meta charset="utf-8">
<title>LumaVek Business Card</title>
<link rel="stylesheet" href="https://fonts.googleapis.com/css2?family=Libre+Baskerville:wght@400;700&display=swap">
<style>
  :root {
    --backdrop: #e4e0d8;
    --card: #ffffff;
    --ink: #1a1a1a;
    --ink-soft: #5a5a5a;
    --shadow: rgba(0, 0, 0, 0.14);
  }
  * { margin: 0; padding: 0; box-sizing: border-box; }
  html, body {
    width: 1200px;
    height: 806px;
    overflow: hidden;
    background: var(--backdrop);
  }
  body {
    font-family: "Libre Baskerville", Baskerville, serif;
    color: var(--ink);
    display: flex;
    align-items: center;
    justify-content: center;
    gap: 60px;
  }
  .card {
    position: relative;
    width: 504px;
    height: 288px;
    background: var(--card);
    box-shadow: 0 6px 22px var(--shadow);
    text-align: center;
  }
  .card-frame {
    position: absolute;
    inset: 14px;
    border: 1.5px solid var(--ink);
    border-radius: 14px;
  }
  /* Front */
  .brand {
    position: absolute;
    top: 84px;
    left: 0;
    right: 0;
    display: flex;
    flex-direction: column;
    align-items: center;
  }
  .brand-name {
    font-size: 20px;
    letter-spacing: 0.02em;
  }
  .brand-mark {
    margin-top: 8px;
    width: 14px;
    height: 14px;
    border-radius: 50%;
    background: var(--ink);
  }
  .brand-line {
    margin-top: 9px;
    font-size: 8px;
    letter-spacing: 0.24em;
    text-transform: uppercase;
    color: var(--ink-soft);
  }
  .services {
    position: absolute;
    bottom: 34px;
    left: 0;
    right: 0;
    font-size: 9px;
    letter-spacing: 0.14em;
    text-transform: uppercase;
    color: var(--ink-soft);
  }
  .services-sep { margin: 0 8px; }
  /* Back */
  .person {
    position: absolute;
    top: 62px;
    left: 0;
    right: 0;
  }
  .person-name {
    font-size: 24px;
    font-weight: 700;
    letter-spacing: 0.05em;
  }
  .person-title {
    margin-top: 4px;
    font-size: 10px;
    letter-spacing: 0.22em;
    text-transform: uppercase;
    color: var(--ink-soft);
  }
  .contact {
    position: absolute;
    top: 146px;
    left: 0;
    right: 0;
    font-size: 12px;
    line-height: 1.7;
  }
  .contact-sep { margin: 0 6px; }
  .registration {
    position: absolute;
    bottom: 32px;
    left: 0;
    right: 0;
    font-size: 10px;
    letter-spacing: 0.04em;
    color: var(--ink-soft);
  }
</style>
</head>
<body>
  <section class="card card-front" aria-label="Card front">
    <div class="card-frame"></div>
    <div class="brand">
      <p class="brand-name">LumaVek</p>
      <span class="brand-mark"></span>
      <p class="brand-line">Photography</p>
    </div>
    <p class="services">Wedding Photography<span class="services-sep">·</span>Portraiture<span class="services-sep">·</span>Photojournalism</p>
  </section>

  <section class="card card-back" aria-label="Card back">
    <div class="card-frame"></div>
    <div class="person">
      <p class="person-name">Dax Pell</p>
      <p class="person-title">Head Photographer</p>
    </div>
    <div class="contact">
      <p>+65 84126079<span class="contact-sep">|</span>tan@lumavek.example</p>
      <p>www.lumavek.example</p>
    </div>
    <p class="registration">Business Reg No: 48271965K</p>
  </section>
</body>
</html>
```